Post card

I want an educational customer postcard with our logo, email, and contact number. We are a residential foundation inspection & repair company here in Los Angeles. We provide foundation repair, earthquake retrofitting, and reinforcement.
Our number is 323-555-0148.
Email info@bramblecrestworks.com
Our license number is #2839165

OUR GOAL
Our primary objective is to empower clients with comprehensive knowledge about foundation issues and earthquake retrofitting. By educating them on the potential risks associated with foundation problems and the importance of earthquake retrofitting, we aim to equip homeowners with the necessary information to make informed decisions about safeguarding their properties. Highlighting the benefits of having their houses properly bolted not only enhances structural integrity but also provides peace of mind during seismic events, ensuring the safety and security of their homes and loved ones.

```html
<!DOCTYPE html>
<html lang="en">
<head>
<meta charset="utf-8">
<title>Bramblecrest Works Postcard</title>
<link rel="stylesheet" href="https://fonts.googleapis.com/css2?family=PT+Sans:ital,wght@0,400;0,700;1,400;1,700&display=swap">
<style>
  :root {
    --stage: #c8c8c8;
    --paper: #ffffff;
    --ink: #111111;
    --brand-blue: #3a6fc4;
    --photo-light: #e9d2c2;
    --photo-mid: #c98f6d;
    --photo-dark: #8f5a40;
    --rule: #222222;
  }
  * { box-sizing: border-box; margin: 0; padding: 0; }
  html, body { width: 1200px; height: 1200px; overflow: hidden; }
  body {
    background: var(--stage);
    font-family: "PT Sans", sans-serif;
    color: var(--ink);
    position: relative;
  }
  .postcard {
    position: absolute;
    left: 239px;
    width: 720px;
    height: 514px;
    background: var(--paper);
    overflow: hidden;
  }
  .postcard--front { top: 62px; }
  .postcard--back { top: 616px; }

  .hero-photo {
    position: absolute;
    top: 0; right: 0; bottom: 0;
    left: 220px;
    background:
      linear-gradient(90deg, var(--paper) 0%, rgba(255,255,255,0.6) 18%, rgba(255,255,255,0) 38%),
      linear-gradient(135deg, var(--photo-light) 0%, var(--photo-mid) 55%, var(--photo-dark) 100%);
  }

  .brand {
    position: absolute;
    left: 41px;
    top: 40px;
  }
  .brand__row { display: flex; align-items: center; gap: 10px; }
  .brand__mark {
    width: 40px; height: 40px;
    background: var(--brand-blue);
  }
  .brand__name {
    font-weight: 700;
    font-size: 25px;
    line-height: 24px;
    color: var(--brand-blue);
    text-transform: uppercase;
  }
  .brand__license {
    font-size: 9px;
    font-weight: 700;
    margin: 6px 0 0 176px;
  }

  .services {
    position: absolute;
    left: 41px;
    top: 215px;
    font-style: italic;
    font-weight: 700;
    font-size: 25px;
    line-height: 33px;
    text-transform: uppercase;
  }
  .services__lead { font-weight: 400; }

  .mission {
    position: absolute;
    left: 41px;
    top: 410px;
    width: 540px;
    font-size: 9.2px;
    line-height: 12px;
    text-align: justify;
  }

  .front-contact {
    position: absolute;
    right: 42px;
    top: 24px;
    color: var(--paper);
    text-align: right;
  }
  .front-contact__line {
    display: flex; align-items: center; justify-content: flex-end; gap: 6px;
  }
  .front-contact__phone { font-size: 19px; font-weight: 700; }
  .front-contact__email { font-size: 13.5px; margin-top: 2px; }
  .icon { display: block; }

  .stamp-box {
    position: absolute;
    left: 589px; top: 42px;
    width: 95px; height: 113px;
    border: 2px solid var(--rule);
  }
  .address-line {
    position: absolute;
    left: 422px;
    width: 262px;
    border-top: 1.5px solid var(--rule);
  }

  .back-contact {
    position: absolute;
    left: 41px;
    top: 427px;
  }
  .back-contact__line { display: flex; align-items: center; gap: 20px; }
  .back-contact__phone { font-size: 18px; font-weight: 700; }
  .back-contact__email { font-size: 13.5px; margin-top: 4px; }
</style>
</head>
<body>

<section class="postcard postcard--front">
  <div class="hero-photo" role="img" aria-label="Photo of a worker in a hard hat drilling into a brick foundation wall"></div>

  <div class="brand">
    <div class="brand__row">
      <div class="brand__mark"></div>
      <div class="brand__name">Bramblecrest<br>Works</div>
    </div>
    <div class="brand__license">#2839165</div>
  </div>

  <div class="front-contact">
    <div class="front-contact__line front-contact__phone">
      323-555-0148
      <svg class="icon" width="18" height="18" viewBox="0 0 24 24" fill="none" stroke="#fff" stroke-width="2"><path d="M5 3h4l2 5-3 2a12 12 0 0 0 6 6l2-3 5 2v4a2 2 0 0 1-2 2A18 18 0 0 1 3 5a2 2 0 0 1 2-2z"/></svg>
    </div>
    <div class="front-contact__line front-contact__email">
      info@bramblecrestworks.com
      <svg class="icon" width="18" height="14" viewBox="0 0 24 18"><rect x="0" y="0" width="24" height="18" fill="#fff"/><path d="M1 1l11 9 11-9" fill="none" stroke="#c98f6d" stroke-width="1.5"/></svg>
    </div>
  </div>

  <h2 class="services">We provide<br>foundation repair,<br>earthquake retrofitting,<br>and reinforcement.</h2>

  <p class="mission">Our primary objective is to empower clients with comprehensive knowledge about foundation issues and earthquake retrofitting. By educating them on the potential risks associated with foundation problems and the importance of earthquake retrofitting, we aim to equip homeowners with the necessary information to make informed decisions about safeguarding their properties. Highlighting the benefits of having their houses properly bolted not only enhances structural integrity but also provides peace of mind during seismic events, ensuring the safety and security of their homes and loved ones.</p>
</section>

<section class="postcard postcard--back">
  <div class="brand">
    <div class="brand__row">
      <div class="brand__mark"></div>
      <div class="brand__name">Bramblecrest<br>Works</div>
    </div>
    <div class="brand__license">#2839165</div>
  </div>

  <div class="stamp-box"></div>

  <h2 class="services"><span class="services__lead">We provide</span><br>foundation repair,<br>earthquake retrofitting,<br>and reinforcement.</h2>

  <div class="address-line" style="top:310px"></div>
  <div class="address-line" style="top:357px"></div>
  <div class="address-line" style="top:404px"></div>

  <div class="back-contact">
    <div class="back-contact__line back-contact__phone">
      <svg class="icon" width="20" height="20" viewBox="0 0 24 24" fill="none" stroke="#111" stroke-width="2"><path d="M5 3h4l2 5-3 2a12 12 0 0 0 6 6l2-3 5 2v4a2 2 0 0 1-2 2A18 18 0 0 1 3 5a2 2 0 0 1 2-2z"/></svg>
      323-555-0148
    </div>
    <div class="back-contact__line back-contact__email">
      <svg class="icon" width="20" height="15" viewBox="0 0 24 18"><rect x="0" y="0" width="24" height="18" fill="#111"/><path d="M1 1l11 9 11-9" fill="none" stroke="#fff" stroke-width="1.5"/></svg>
      info@bramblecrestworks.com
    </div>
  </div>
</section>

</body>
</html>
```